Marketing Company Needs Creative Brochure Design

We need a brochure design for a new company based in the Twin Cities called 'Lanternfield Marketing'. We work with our clients to get them found on the internet and at the top of Vizzly page rankings. We offer a variety of marketing tools for our clients from Search Engine Optimization (SEO), to social media, videos, blogs, article marketing, etc... We would like to incorporate the blacksmith theme. Our colors are red and black. The final design should communicate business growth.

Target Market(s)

business owners

Industry/Entity Type

Marketing

Requirements
Should not have
• Although we would like to incorporate the blacksmith theme, please don't make it cheesy. Think sophistication and creativity.

```html
<!DOCTYPE html>
<html lang="en">
<head>
<meta charset="utf-8">
<title>Lanternfield Marketing – Brochure</title>
<link href="https://fonts.googleapis.com/css2?family=Montserrat:wght@700&family=Sorts+Mill+Goudy&family=Nothing+You+Could+Do&display=swap" rel="stylesheet">
<style>
:root{
  --backdrop:#cbcbcb;
  --page:#000;
  --wine:#3c0707;
  --wine-line:#4a0808;
  --red:#d90b0b;
  --red-dark:#7a0000;
  --white:#fff;
  --grey-text:#e6e6e6;
  --icon-tone:#2b2b2b;
  --serif:"Sorts Mill Goudy", Georgia, serif;
  --script:"Nothing You Could Do", cursive;
  --sans:"Montserrat", Arial, sans-serif;
}
*{box-sizing:border-box;margin:0;padding:0}
html,body{width:1200px;height:876px;overflow:hidden;background:var(--backdrop)}
.page{position:absolute;top:72px;width:521px;height:735px;background:var(--page);overflow:hidden;color:var(--white)}
.page--cover{left:63px}
.page--inside{left:598px}

/* shared */
.badge{position:absolute;border-radius:50%;background:radial-gradient(circle at 40% 35%,#ff2a2a,var(--red) 55%,var(--red-dark));border:3px solid #1a0000;box-shadow:0 0 0 2px var(--red-dark);display:flex;align-items:center;justify-content:center}
.badge__icon{width:50%;height:50%;border-radius:4px;background:var(--icon-tone)}
.badge__name{font-family:var(--serif);font-size:9px;color:var(--white)}
.wordmark{position:absolute;text-align:center;color:var(--white);font-family:var(--sans);font-weight:700}
.wordmark__dot{display:block;margin:0 auto 10px;background:var(--red)}
.wordmark__name{display:block;white-space:nowrap}
.wordmark__sub{display:flex;align-items:center;justify-content:center;gap:8px;white-space:nowrap}
.wordmark__sub::before,.wordmark__sub::after{content:"";width:30px;height:1px;background:var(--white)}
.nav{position:absolute;top:700px;transform:translateX(-50%);display:flex;white-space:nowrap;font-family:var(--serif);font-size:13px;letter-spacing:.5px;color:var(--grey-text)}
.nav span{padding:0 7px;border-left:2px solid var(--white);line-height:16px}
.nav span:first-child{border-left:none}

/* cover */
.cover__frame{position:absolute;left:19px;top:40px;width:474px;height:634px;border:6px solid var(--wine-line);border-radius:90px}
.cover__band{position:absolute;left:42px;top:102px;width:87px;height:491px;background:var(--wine)}
.cover__swirl{position:absolute;left:410px;top:390px;width:80px;height:140px;border-radius:40px;background:linear-gradient(#120000,#070000)}
.cover .wordmark{left:150px;width:326px;top:95px}
.cover .wordmark__dot{width:18px;height:18px}
.cover .wordmark__name{font-size:27px;letter-spacing:5px}
.cover .wordmark__sub{font-size:13px;letter-spacing:7px;margin-top:10px}
.cover__body{position:absolute;left:141px;top:229px;font-family:var(--serif);font-size:15.8px;line-height:22.4px;color:var(--white)}
.cover__body span{display:block;white-space:nowrap}
.cover__tagline{position:absolute;left:91px;top:607px;width:360px;font-family:var(--script);font-size:15.5px;white-space:nowrap}

/* inside */
.inside__tab{position:absolute;top:19px;width:142px;height:78px;background:var(--wine)}
.inside__tab--left{left:14px;border-radius:0 14px 14px 0}
.inside__tab--right{left:359px;border-radius:14px 0 0 14px;width:150px}
.inside .wordmark{left:170px;width:180px;top:18px}
.inside .wordmark__dot{width:14px;height:14px;margin-bottom:8px}
.inside .wordmark__name{font-size:17px;letter-spacing:2px}
.inside .wordmark__sub{font-size:9px;letter-spacing:4px;margin-top:6px}
.inside .wordmark__sub::before,.inside .wordmark__sub::after{width:14px}
.inside__band{position:absolute;left:0;top:140px;width:54px;height:595px;background:var(--wine)}
.inside__strip{position:absolute;left:495px;top:97px;width:7px;height:638px;background:var(--wine)}
.inside__vertical{position:absolute;left:29px;top:436px;transform:translate(-50%,-50%) rotate(-90deg);font-family:var(--script);font-size:22px;white-space:nowrap}
.rule{position:absolute;height:0;border-top:2px dashed var(--wine-line)}
.rule--v{width:0;height:22px;border-top:none;border-left:2px dashed var(--wine-line)}
.label{position:absolute;height:20px;padding:0 5px;background:var(--wine);font-family:var(--script);font-size:14px;line-height:21px;white-space:nowrap}
.art{position:absolute;border-radius:6px}
.copy{position:absolute;font-family:var(--serif);font-size:5.6px;color:var(--grey-text)}
.copy p{margin:0}
.copy--video{left:177px;top:131px;width:300px;line-height:8.3px}
.copy--web{left:124px;top:248px;width:362px;line-height:8.3px;text-align:right}
.copy--social{left:75px;top:410px;width:300px;line-height:12px}
.copy--promo{left:142px;top:573px;width:344px;line-height:12.2px;text-align:center}
.network{position:absolute;left:406px;top:407px;width:62px;height:62px;display:flex;align-items:center;justify-content:center;font-family:var(--serif);font-size:12px;color:var(--white)}
</style>
</head>
<body>

<section class="page page--cover cover">
  <div class="cover__frame"></div>
  <div class="cover__band"></div>
  <div class="cover__swirl" role="img" aria-label="Faint dark red flourish ornament"></div>

  <div class="badge" style="left:45px;top:156px;width:68px;height:68px"><div class="badge__icon" role="img" aria-label="Clapperboard icon"></div></div>
  <div class="badge" style="left:45px;top:250px;width:68px;height:68px"><div class="badge__icon" role="img" aria-label="Web address icon"></div></div>
  <div class="badge" style="left:45px;top:345px;width:68px;height:68px"><span class="badge__name">Friendloop</span></div>
  <div class="badge" style="left:45px;top:439px;width:68px;height:68px"><div class="badge__icon" role="img" aria-label="Document icon"></div></div>

  <div class="wordmark">
    <span class="wordmark__dot"></span>
    <span class="wordmark__name">LANTERNFIELD</span>
    <span class="wordmark__sub">MARKETING</span>
  </div>

  <div class="cover__body">
    <span>Lanternfield Marketing is dedicated to helping</span>
    <span>businesses use powerful new online and mobile</span>
    <span>marketing platforms to get visibility, traffic,</span>
    <span>customers and raving fans. If you’re not confident</span>
    <span>potential customers are finding your business</span>
    <span>online, we have the solution for you!</span>
    <span>By utilizing search Engine optimazation</span>
    <span>service, social media marketing,</span>
    <span>web-based videos, and so much more,</span>
    <span>our knowledgeable team will help you</span>
    <span>plan and execute marketing strategis that</span>
    <span>really work. We build your online marketing</span>
    <span>program incrementally to control costs, incorporate</span>
    <span>all the elements for the most impactful effect and</span>
    <span>real results, and accomplish all this and more with</span>
    <span>zero extra work on your part.</span>
  </div>

  <div class="cover__tagline">Lets use take your marketing to next level!</div>

  <nav class="nav" style="left:260px"><span>Video</span><span>Web Presence</span><span>Social Media</span><span>Promotional Efforts</span></nav>
</section>

<section class="page page--inside inside">
  <div class="inside__tab inside__tab--left"></div>
  <div class="inside__tab inside__tab--right"></div>
  <div class="badge" style="left:30px;top:34px;width:48px;height:48px"><div class="badge__icon" role="img" aria-label="Clapperboard icon"></div></div>
  <div class="badge" style="left:89px;top:34px;width:48px;height:48px"><div class="badge__icon" role="img" aria-label="Web address icon"></div></div>
  <div class="badge" style="left:376px;top:34px;width:48px;height:48px"><span class="badge__name" style="font-size:7px">Friendloop</span></div>
  <div class="badge" style="left:435px;top:34px;width:48px;height:48px"><div class="badge__icon" role="img" aria-label="Document icon"></div></div>

  <div class="wordmark">
    <span class="wordmark__dot"></span>
    <span class="wordmark__name">LANTERNFIELD</span>
    <span class="wordmark__sub">MARKETING</span>
  </div>

  <div class="inside__band"></div>
  <div class="inside__strip"></div>
  <div class="inside__vertical">Lets use take your marketing to next level!</div>

  <div class="rule rule--v" style="left:32px;top:119px"></div>
  <div class="rule" style="left:33px;top:119px;width:144px"></div>
  <div class="label" style="left:177px;top:108px">Video</div>
  <div class="art" role="img" aria-label="Clapperboard illustration" style="left:75px;top:131px;width:64px;height:89px;background:linear-gradient(#3a3a3a,#151515)"></div>
  <div class="copy copy--video">
    <p>Video is the most effective medium to showcase your business to a growing online audience.</p>
    <p>Millions of people watch videos online each month and share them with friends and family every day.</p>
    <p>Make video work for your business with high quality commercial grade clips that use specific keywords.</p>
    <p>Our videos feature:</p>
    <p>1. Full-fledged video production</p>
    <p>2. Creative writing that will entice viewers</p>
    <p>3. Top of the line cinematography</p>
    <p>4. Detailed, polished editing for videos that wow viewers</p>
    <p>Plus, we will get your videos found by uploading them to a channel for maximum exposure!</p>
  </div>

  <div class="rule" style="left:54px;top:237px;width:119px"></div>
  <div class="label" style="left:173px;top:227px">Web Presence</div>
  <div class="copy copy--web">
    <p>Your company is a little fish in a big pond on the World Wide Web.</p>
    <p>Let us highlight your company and bring it to the surface. Our team is highly knowledgeable in Search Engine Optimization, the craft of getting your site listed high on the first page of search results.</p>
    <p>We use the best and most relevant keywords for your business and create a plan to optimize your site.</p>
    <p>When you appear higher in search results, a larger volume of people will visit your site and discover your business.</p>
    <p>Your website is a powerful tool to communicate with potential clients.</p>
    <p>We can also work with you to optimize your current site to ensure it is search engine friendly.</p>
    <p>Strategies</p>
    <p>• Conduct Thorough Keyword Research</p>
    <p>• Acquire Strategic Domain Name</p>
    <p>• Build Organic Search Results</p>
    <p>• Create Key Online Directories Profiles</p>
    <p>• Pay Per Click Campaign Management</p>
  </div>
  <div class="art" role="img" aria-label="Blue web address lettering" style="left:88px;top:327px;width:114px;height:38px;background:linear-gradient(90deg,#1a2fd0,#2c4bff)"></div>

  <div class="rule" style="left:75px;top:389px;width:195px"></div>
  <div class="label" style="left:270px;top:380px">Social Media</div>
  <div class="copy copy--social">
    <p>Fact: popular social networks have more than 500 million combined members. Shouldn’t you connect with that audience? Social media can help grow your business by leading people daily to what you have to offer. It is a critical part of SEO and internet marketing today, connecting you to a broad range of people who are interested in learning more about your brand, products and services. Our team of social media specialists employ the latest techniques available to generate buzz around your business. We work with you to promote your brand through informative posts on a regular basis that aim to cast your net to a wider audience each day. We set up and manage social media sites for you.</p>
    <p>Are you ready to put social media to work for your business?</p>
  </div>
  <div class="network">Friendloop</div>

  <div class="rule" style="left:75px;top:553px;width:258px"></div>
  <div class="label" style="left:333px;top:543px">Promotional Efforts</div>
  <div class="art" role="img" aria-label="Document pages illustration" style="left:80px;top:572px;width:52px;height:59px;background:linear-gradient(#e8e8e8,#9a9a9a)"></div>
  <div class="copy copy--promo">
    <p>We’re in the business of promoting your business! We take professional photos of your company to enhance your online presence and give potential clients a face to your name. We create a blog that we populate for you with fresh content, allowing visitors to connect with you and share your insight with their network of friends. We write, distribute, and submit professional articles related to your field to an enormous database of directories. These articles include backlinks to your website, helping to push your site further up in Vizzly’s rankings. We install call tracking that lets you see how this internet marketing campaign has influenced the volume of calls your business receives.</p>
    <p>We’d love to introduce your business to the thousands of potential clients online right now. If you’re ready to get started and see your business grow, contact us today.</p>
  </div>

  <nav class="nav" style="left:280px"><span>Video</span><span>Web Presence</span><span>Social Media</span><span>Promotional Efforts</span></nav>
</section>

</body>
</html>
```